Computer screen desktop background design for dentists orthodontic office PCs

We need a new design to use as the Windows desktop background picture for the PC workstations in a dentists orthodontic office.
The design should be vector graphics.
The aspect ratio should reflect the monitor size (Resolution: 1920x1200).
In the uploaded files you can find the logo, the fonts and the design of the business card.
The design should not be brighter than the Windows 10 background picture (monitor lifetime).

The office logo must be the dominating part of the design (see uploaded files).

You don't need to use the same fonts, but the used fonts have to be in harmony with the fonts used in the logo and the business card.
The colors used have to be in harmony with the logo.
All the text below must be on the design.
The logical text groups are separated by empty lines.

Kieferorthopädie Brunnweid

Dr. med. dent. Anton Vrabec
Fachzahnarzt für Kieferorthopädie (CH) (Important information!)

Please make something cool and modern that attracts the patient's attraction when seen on the monitor screen.

Target Market(s)

dentists orthodontic office

Industry/Entity Type

Computer

Font styles to use
Sans Serif

Colors

Designer to choose colors to be used in the design.

Requirements
Must have
• The design should be vector graphics.
• The aspect ratio should reflect the monitor size (Resolution: 1920x1200).
• In the uploaded files you can find the logo, the fonts and the design of the business card.
• The design should not be brighter than the Windows 10 background picture (monitor lifetime).
• The office logo must be the dominating part of the design (see uploaded files).
• You don't need to use the same fonts, but the used fonts have to be in harmony with the fonts used in the logo and the business card.
• The colors used have to be in harmony with the logo.
• All the text below must be on the design.
• The logical text groups are separated by empty lines.
• Kieferorthopädie Brunnweid
• Dr. med. dent. Anton Vrabec
• Fachzahnarzt für Kieferorthopädie (CH) (Important information!)
• Adobe Illustrator source files
Nice to have
• Please make something cool and modern that attracts the patient's attraction when seen on the monitor screen.
Should not have

```html
<!DOCTYPE html>
<html lang="de">
<head>
<meta charset="utf-8">
<title>Kieferorthopädie Brunnweid – Desktop</title>
<link rel="stylesheet" href="https://fonts.googleapis.com/css2?family=Saira+Semi+Condensed:wght@400;600;700&family=Saira+Condensed:wght@400&display=swap">
<style>
  :root {
    --page-bg: #e9e9ea;
    --paper-top: #f4f4f5;
    --paper-bottom: #e3e4e6;
    --brand-blue: #0b86d6;
    --brand-blue-deep: #0a6fbf;
    --brand-navy: #2b2166;
    --text-grey: #2f2f33;
  }
  html, body {
    margin: 0;
    width: 1200px;
    height: 1000px;
    overflow: hidden;
    background: var(--page-bg);
  }
  .canvas {
    position: relative;
    width: 1200px;
    height: 1000px;
  }
  .wallpaper {
    position: absolute;
    left: 0;
    top: 125px;
    width: 1200px;
    height: 750px;
    overflow: hidden;
    background: linear-gradient(180deg, var(--paper-top), var(--paper-bottom));
  }
  .wallpaper-shapes {
    position: absolute;
    inset: 0;
  }
  .brand {
    position: absolute;
    left: 78px;
    top: 118px;
    display: flex;
    align-items: center;
    gap: 26px;
  }
  .brand-dot {
    width: 110px;
    height: 110px;
    border-radius: 50%;
    background: var(--brand-navy);
  }
  .brand-name {
    font-family: "Saira Semi Condensed", sans-serif;
    font-weight: 700;
    font-size: 44px;
    color: var(--brand-navy);
    letter-spacing: 0.2px;
  }
  .doctor {
    position: absolute;
    left: 78px;
    top: 348px;
  }
  .doctor-name {
    margin: 0;
    font-family: "Saira Semi Condensed", sans-serif;
    font-weight: 600;
    font-size: 52px;
    line-height: 1.1;
    color: var(--brand-blue);
  }
  .doctor-title {
    margin: 6px 0 0;
    font-family: "Saira Condensed", sans-serif;
    font-weight: 400;
    font-size: 30px;
    color: var(--text-grey);
  }
</style>
</head>
<body>
<div class="canvas">
  <div class="wallpaper">
    <svg class="wallpaper-shapes" width="1200" height="750" viewBox="0 0 1200 750" aria-hidden="true">
      <defs>
        <linearGradient id="blueField" x1="0" y1="0" x2="1" y2="1">
          <stop offset="0" stop-color="#0b8ee0"/>
          <stop offset="1" stop-color="#0a6fbf"/>
        </linearGradient>
      </defs>
      <path d="M800 0 C 905 250, 790 560, 470 750 L 1200 750 L 1200 0 Z" fill="url(#blueField)"/>
      <path d="M800 0 C 905 250, 790 560, 470 750" fill="none" stroke="#ffffff" stroke-width="6"/>
      <path d="M748 0 C 830 110, 850 260, 820 390 C 872 250, 858 110, 792 0 Z" fill="var(--brand-navy)"/>
    </svg>

    <div class="brand">
      <div class="brand-dot"></div>
      <div class="brand-name">Kieferorthopädie Brunnweid</div>
    </div>

    <div class="doctor">
      <p class="doctor-name">Dr. med. dent. Anton Vrabec</p>
      <p class="doctor-title">Fachzahnarzt für Kieferorthopädie (CH)</p>
    </div>
  </div>
</div>
</body>
</html>
```